Label for Refill packaging eco-conscious beauty brand

We need a label for our refill pouch. Velvet Harbor is an unscented conditioner formulated using the finest healthy & pure ingredients, free of chemicals and harmful toxins. As a minimalist beauty brand we are proud to be certified with TPL, VerdaSeal and Silver Fawn.

We already have the pouches and an exciting label for our regular bottles.
We choose a kraft brown packing for the refill pouch and would like something minimalist but elegant for the label.

```html
<!DOCTYPE html>
<html lang="en">
<head>
<meta charset="utf-8">
<title>Velvet Harbor – refill pouch label</title>
<link rel="stylesheet" href="https://fonts.googleapis.com/css2?family=Raleway:ital,wght@0,400;0,500;1,400;1,500&display=swap">
<style>
  :root {
    --page: #f6f6f5;
    --label: #d7d4ce;
    --leaf: #c9c5bd;
    --gold-dark: #c8961c;
    --gold-light: #f3d55e;
    --title: #7a6468;
    --body: #3b2a1f;
    --white: #ffffff;
  }
  * { margin: 0; padding: 0; box-sizing: border-box; }
  html, body {
    width: 1126px; height: 1200px; overflow: hidden;
    background: var(--page);
    font-family: "Raleway", sans-serif;
  }
  .label {
    position: absolute; left: 200px; top: 32px;
    width: 725px; height: 1135px;
  }
  .label-shape { position: absolute; inset: 0; }
  .herb-sprig {
    position: absolute; left: 30px; top: 180px;
    width: 640px; height: 940px;
    background: radial-gradient(ellipse at 55% 55%, var(--leaf) 0%, rgba(201,197,189,0.45) 45%, rgba(215,212,206,0) 72%);
    opacity: 0.7;
  }
  .brand-panel {
    position: absolute; left: 264px; top: 2px;
    width: 213px; height: 375px;
    background: linear-gradient(160deg, var(--gold-light) 0%, var(--gold-dark) 45%, var(--gold-light) 70%, var(--gold-dark) 100%);
    display: flex; flex-direction: column; justify-content: flex-end; align-items: center;
    padding-bottom: 48px;
  }
  .brand-name {
    color: var(--white); font-weight: 400; font-size: 38px;
    line-height: 1.05; text-align: center; letter-spacing: 1px;
  }
  .product-name {
    position: absolute; left: 0; width: 100%; top: 488px;
    text-align: center; color: var(--title);
    font-weight: 500; font-size: 76px; line-height: 1.03;
  }
  .product-type {
    position: absolute; left: 0; width: 100%; top: 705px;
    text-align: center; color: var(--body);
  }
  .product-type .en { font-size: 40px; font-weight: 400; line-height: 1.1; }
  .product-type .fr { font-size: 29px; font-style: italic; font-weight: 500; line-height: 1.1; }
  .net-volume {
    position: absolute; left: 0; width: 100%; top: 900px;
    text-align: center; color: var(--title);
    font-family: Arial, "Helvetica Neue", sans-serif; font-size: 28px;
  }
</style>
</head>
<body>
  <section class="label">
    <svg class="label-shape" width="725" height="1135" viewBox="0 0 725 1135" aria-hidden="true">
      <path d="M0 0 H725 V1030 Q362.5 1190 0 1030 Z" fill="var(--label)"/>
    </svg>
    <div class="herb-sprig" role="img" aria-label="Faint line drawing of a herb sprig behind the text"></div>
    <div class="brand-panel">
      <p class="brand-name">SOLEN<br>Maren</p>
    </div>
    <h1 class="product-name">Velvet<br>Harbor</h1>
    <div class="product-type">
      <p class="en">unscented hair conditioner</p>
      <p class="fr">apres-shampoing non parfume</p>
    </div>
    <p class="net-volume">238ml e/8ft oz.</p>
  </section>
</body>
</html>
```